Gift card design to reflect the theme from our overhead business sign

We need a gift card that aligns with our colors used for the sign. Since I am not sure what you're able to do with the limited space, if you think you can create a miniature version of the sign and add the words "Gift Card" to it. I'd like to see it. I have also uploaded the original logo we use as an other variable to use in place the horizontal one on the sign. That might be alright too. Give me a few options to consider.

Then for the back of the card there may be some legal requirements for the wording. I'll get back to you on that. First, let's focus on the design.

Also, i am sending the requirements for "Quorix" who will be the processor for the card. I will be doing custom cards so pay attention to page 4.

After the gift card, I will sending you the front of the store image with the sign in place, so you can come up with some ideas for a simple window design to go across all the windows.

How fast can you get back to me? Unlike the sign, I'm sort of in a time crunch.

Oh, one other thing, I want to change the pink in our current logo to the pink you used in the sign. So if you use our standard logo, please change the pink to the on you used for the sign.

```html
<!DOCTYPE html>
<html lang="en">
<head>
<meta charset="utf-8">
<title>The Sweet Parlor Gift Card</title>
<link rel="stylesheet" href="https://fonts.googleapis.com/css2?family=Comfortaa:wght@700&display=swap">
<style>
  :root {
    --backdrop: #e4e4e4;
    --lime: #b3d44a;
    --pink: #ee3d96;
    --pink-shade: #b3286f;
    --orange: #f48a2c;
    --white: #ffffff;
  }
  * { margin: 0; padding: 0; box-sizing: border-box; }
  html, body {
    width: 1200px;
    height: 960px;
    overflow: hidden;
    background: var(--backdrop);
  }
  .canvas {
    position: relative;
    width: 1200px;
    height: 960px;
    display: flex;
    align-items: center;
    justify-content: center;
  }
  .gift-card {
    position: relative;
    width: 788px;
    height: 492px;
    border-radius: 18px;
    background: var(--lime);
    font-family: "Comfortaa", sans-serif;
    color: var(--white);
  }
  .gift-card__band {
    position: absolute;
    inset: 29px;
    background: var(--pink);
  }
  .gift-card__frame {
    position: absolute;
    inset: 12px;
    border: 13px solid var(--orange);
  }
  .gift-card__title {
    position: absolute;
    left: 0;
    right: 0;
    top: 140px;
    text-align: center;
    font-size: 128px;
    font-weight: 700;
    line-height: 1;
    letter-spacing: -2px;
    text-shadow: 16px 30px 0 var(--pink-shade);
  }
  .gift-card__url {
    position: absolute;
    left: 68px;
    top: 403px;
    font-size: 19px;
    font-weight: 700;
    letter-spacing: 0.2px;
  }
  .brand {
    position: absolute;
    right: 66px;
    top: 362px;
    display: flex;
    align-items: center;
    gap: 10px;
  }
  .brand__mark {
    width: 14px;
    height: 14px;
    border-radius: 50%;
    background: var(--white);
  }
  .brand__name {
    font-size: 24px;
    font-weight: 700;
    line-height: 1.1;
    text-align: right;
  }
</style>
</head>
<body>
  <main class="canvas">
    <article class="gift-card">
      <div class="gift-card__band">
        <div class="gift-card__frame"></div>
      </div>
      <h1 class="gift-card__title">Gift Card</h1>
      <p class="gift-card__url">sweetparlorbakes.com</p>
      <div class="brand">
        <span class="brand__mark"></span>
        <span class="brand__name">The Sweet<br>Parlor</span>
      </div>
    </article>
  </main>
</body>
</html>
```